Update Business Card Design

I'm looking to update my business cards. Attached is a photo of the current design. I like the black side so that does not have to be update. The white side needs to be updated. I want the design to be modern and minimalistic.
I am a lawyer and my firm's website is www.brennoxlegalco.com (for reference).
My firm's logo has a horizontal version (which is on the black side of the card) and a vertical version (on the white side). I would prefer to keep the vertical version on the white side and horizontal version on the black side (the logo files are attached).

I am open to redesigning the black side also. I would like one side to have the horizontal logo and the other to have the vertical logo.

```html
<!DOCTYPE html>
<html lang="en">
<head>
<meta charset="utf-8">
<title>Brennox Legal Co. — Business Card</title>
<link rel="stylesheet" href="https://fonts.googleapis.com/css2?family=Merriweather:wght@900&family=Poppins:wght@400;500&display=swap">
<style>
  :root {
    --backdrop: #9b9b9b;
    --card-white: #ffffff;
    --card-black: #1c1c1b;
    --brand-blue: #00b5e2;
    --ink: #1d1d1d;
    --rule-grey: #5d5d5d;
  }
  * { margin: 0; padding: 0; box-sizing: border-box; }
  html, body { width: 1093px; height: 1200px; overflow: hidden; }
  body {
    background: var(--backdrop);
    position: relative;
    font-family: "Poppins", sans-serif;
    color: var(--ink);
  }
  .card {
    position: absolute;
    left: 264px;
    width: 580px;
    height: 356px;
    border-radius: 27px;
    overflow: hidden;
  }
  .card::after {
    content: "";
    position: absolute;
    left: 0; right: 0; bottom: 0;
    height: 9px;
    background: var(--brand-blue);
  }
  .card--front { top: 226px; background: var(--card-white); }
  .card--back  { top: 621px; background: var(--card-black); }

  .name-marker {
    position: absolute; left: 0; top: 49px;
    width: 14px; height: 36px;
    background: var(--brand-blue);
  }
  .person { position: absolute; left: 28px; top: 46px; }
  .person__name {
    font-family: "Merriweather", serif;
    font-weight: 900;
    font-size: 20px;
    line-height: 24px;
    color: var(--brand-blue);
    letter-spacing: 0.2px;
  }
  .person__title {
    font-size: 16px;
    line-height: 20px;
    color: var(--ink);
  }

  .firm-vertical {
    position: absolute; right: 28px; top: 40px;
    width: 140px;
    display: flex; flex-direction: column; align-items: flex-end;
  }
  .firm-vertical__square {
    width: 56px; height: 56px;
    background: var(--brand-blue);
    margin-right: 40px;
  }
  .firm-vertical__rule {
    width: 136px; height: 2px;
    background: var(--rule-grey);
    margin: 28px -8px 10px 0;
  }
  .firm-name {
    font-weight: 500;
    color: var(--brand-blue);
    text-align: right;
    line-height: 1.1;
  }
  .firm-vertical .firm-name { font-size: 22px; }

  .contacts {
    position: absolute; left: 28px; top: 239px;
    list-style: none;
    font-size: 16.5px;
    line-height: 21px;
  }
  .contacts li { display: flex; align-items: center; gap: 9px; }
  .contacts svg { width: 17px; height: 17px; fill: var(--brand-blue); flex: none; }

  .address {
    position: absolute; right: 30px; top: 260px;
    font-style: normal;
    text-align: right;
    font-size: 16.5px;
    line-height: 21px;
  }

  .firm-horizontal {
    position: absolute; left: 125px; top: 131px;
    display: flex; align-items: center;
  }
  .firm-horizontal__square {
    width: 92px; height: 92px;
    background: var(--brand-blue);
  }
  .firm-horizontal__rule {
    width: 1px; height: 94px;
    background: var(--rule-grey);
    margin: 0 18px 0 34px;
  }
  .firm-horizontal .firm-name { font-size: 38px; text-align: left; }
</style>
</head>
<body>
  <section class="card card--front">
    <span class="name-marker"></span>
    <div class="person">
      <h1 class="person__name">DANIEL CORVELL</h1>
      <p class="person__title">Attorney at Law</p>
    </div>

    <div class="firm-vertical">
      <span class="firm-vertical__square"></span>
      <span class="firm-vertical__rule"></span>
      <p class="firm-name">BRENNOX<br>LEGAL CO.</p>
    </div>

    <ul class="contacts">
      <li>
        <svg viewBox="0 0 16 16" aria-hidden="true"><path d="M4 0h8a1 1 0 0 1 1 1v14a1 1 0 0 1-1 1H4a1 1 0 0 1-1-1V1a1 1 0 0 1 1-1zm.5 1.5v11h7v-11zM8 13.3a.8.8 0 1 0 0 1.6.8.8 0 0 0 0-1.6z"/></svg>
        555.210.4381
      </li>
      <li>
        <svg viewBox="0 0 16 16" aria-hidden="true"><path d="M3.6 1l2.2 2.6-1.3 1.6c.8 2 2.3 3.6 4.3 4.4l1.6-1.3L13 10.5l-1.4 2.6c-5.2-.3-9.3-4.5-9.6-9.6z"/><path d="M9 1a6 6 0 0 1 6 6h-1.3A4.7 4.7 0 0 0 9 2.3zm0 2.6A3.4 3.4 0 0 1 12.4 7h-1.3A2.1 2.1 0 0 0 9 4.9z"/></svg>
        555.318.6624
      </li>
      <li>
        <svg viewBox="0 0 16 16" aria-hidden="true"><path d="M4 0h8v4H4zM1 5h14a1 1 0 0 1 1 1v6h-3v4H3v-4H0V6a1 1 0 0 1 1-1zm4 5v4.5h6V10zm1 1h4v1H6zm0 1.8h4v1H6z"/></svg>
        555.318.6650
      </li>
      <li>
        <svg viewBox="0 0 16 16" aria-hidden="true"><path d="M0 3h16v10H0zm1.5 1.3v.2L8 9l6.5-4.5v-.2zm0 2v5.4l3.6-2.9zm13 0l-3.6 2.5 3.6 2.9zM6.2 9.6l-4.5 2.1h12.6L9.8 9.6 8 10.9z"/></svg>
        daniel@BrennoxLegalCo.com
      </li>
    </ul>

    <address class="address">
      118 Harlow Avenue<br>
      Suite 340 Westbrook<br>
      CA 90512
    </address>
  </section>

  <section class="card card--back">
    <div class="firm-horizontal">
      <span class="firm-horizontal__square"></span>
      <span class="firm-horizontal__rule"></span>
      <p class="firm-name">BRENNOX<br>LEGAL CO.</p>
    </div>
  </section>
</body>
</html>
```